QUOTE Graphics for Summer Challenge

I would like to put these quotes over one of the pictures attached; For Instagram, use new size: 4:5 (1080 x 1350 pixels). One Quote per picture, and I want the quote to be bold or easy to read as well. I provided a few reference graphics that I really like as examples below.
All of the pictures are attached; you can pick any photo and add one quote to it; but no stock photography
All the quotes are in the attached WORD document

```html
<!DOCTYPE html>
<html lang="en">
<head>
<meta charset="utf-8">
<title>Sun Glow Summer Reset – Quote Graphics</title>
<link href="https://fonts.googleapis.com/css2?family=Oswald:wght@500;600;700&family=DM+Serif+Display&family=Archivo+Black&display=swap" rel="stylesheet">
<style>
  :root{
    --page:#e9eaec;
    --magenta:#d8006c;
    --blush:#fde3ef;
    --band-pink:#ff9fcf;
    --frame:#ff9fd0;
    --ink:#111111;
    --sky:#8fc3e6;
    --pool:#4aa8d8;
    --skin:#8a5a3c;
  }
  *{box-sizing:border-box;margin:0;padding:0}
  html,body{width:1200px;height:624px;overflow:hidden;background:var(--page)}
  .board{position:relative;width:1200px;height:624px}
  .post{position:absolute;width:212px;height:264px;background:var(--magenta);overflow:hidden;box-shadow:0 1px 3px rgba(0,0,0,.12);
    font-family:"Oswald",sans-serif;color:var(--ink)}
  .post__photo{position:absolute;left:102px;top:0;right:0;bottom:0;
    background:linear-gradient(180deg,var(--sky) 0%,#b9d9ec 28%,var(--skin) 45%,#6e4530 72%,var(--pool) 100%)}
  .post__photo--warm{background:linear-gradient(180deg,#9fc6dc 0%,#7b8a6a 25%,#8a6a48 50%,#7a5a3a 80%,#5b86a8 100%)}
  .post__photo--garden{background:linear-gradient(180deg,#c9d4cf 0%,#8a6a4a 40%,#7a4f30 70%,#6e9a4a 100%)}
  .post__frame{position:absolute;left:30px;width:72px;border-left:1.5px solid var(--frame)}
  .post__frame--top{top:16px;height:40px;border-top:1.5px solid var(--frame)}
  .post__frame--bottom{top:208px;height:38px;border-bottom:1.5px solid var(--frame)}
  .post__card{position:absolute;left:18px;top:54px;width:101px;height:156px;background:var(--blush);border-radius:5px;opacity:.96}
  .post__text{position:absolute;left:26px;white-space:nowrap;letter-spacing:-.2px}
  .post__band{position:absolute;left:0;width:119px;height:13px;background:var(--band-pink);
    font-weight:700;font-size:10px;line-height:13px;padding-left:29px;white-space:nowrap}
  .post__handle{position:absolute;left:18px;width:101px;text-align:center;font-weight:500;font-size:6.5px;white-space:nowrap}
  .w7{font-weight:700}.w6{font-weight:600}.w5{font-weight:500}
  .serif{font-family:"DM Serif Display",serif;font-weight:400}
  .wide{font-family:"Archivo Black",sans-serif}
</style>
</head>
<body>
<main class="board">

  <!-- Row 1 -->
  <article class="post" style="left:30px;top:38px">
    <div class="post__photo" role="img" aria-label="Woman in leopard bikini seated at poolside"></div>
    <div class="post__frame post__frame--top"></div><div class="post__frame post__frame--bottom"></div>
    <div class="post__card"></div>
    <h2 class="post__text serif" style="top:64px;font-size:15px;line-height:15px">Feeling<br>Bloated,<br>Sluggish,<br>and too Big?</h2>
    <p class="post__text w5" style="top:127px;font-size:13px;line-height:14px">Your Detox<br>starts now.</p>
    <div class="post__band" style="top:158px">Comment SUMMER</div>
    <p class="post__text w5" style="left:29px;top:172px;font-size:7px;line-height:8.5px">to join THE SUN GLOW<br>SUMMER RESET</p>
    <p class="post__handle" style="top:195px">@Maya Rivers Online</p>
  </article>

  <article class="post" style="left:267px;top:38px">
    <div class="post__photo" role="img" aria-label="Woman in black bikini standing in a pool"></div>
    <div class="post__frame post__frame--top"></div><div class="post__frame post__frame--bottom"></div>
    <div class="post__card"></div>
    <h2 class="post__text w5" style="top:69px;font-size:11.5px;line-height:13.5px">The Scale keeps<br>Climbing and<br>nothing's working?</h2>
    <p class="post__text w6" style="top:115px;font-size:12.5px;line-height:14px">This challenge<br>is your <span class="w7">LIFELINE.</span></p>
    <div class="post__band" style="top:151px;height:14px;line-height:14px;font-size:11px">Comment SUN GLOW</div>
    <p class="post__text w6" style="left:29px;top:169px;font-size:12.5px">to join now!</p>
    <p class="post__handle" style="top:197px">@Maya Rivers Online</p>
  </article>

  <article class="post" style="left:498px;top:38px">
    <div class="post__photo post__photo--warm" role="img" aria-label="Smiling woman in olive cut-out swimsuit and mesh cover-up"></div>
    <div class="post__frame post__frame--top"></div><div class="post__frame post__frame--bottom"></div>
    <div class="post__card"></div>
    <h2 class="post__text w7" style="top:65px;font-size:16.5px;line-height:15.5px">Your Belly<br>Bloat &amp;<br>Stubborn<br>weight Gain</h2>
    <p class="post__text w6" style="left:27px;top:130px;font-size:8px;line-height:10px">aren't going anywhere…<br>unless you do<br>something Different.</p>
    <div class="post__band" style="top:163px;height:14px;line-height:14px;font-size:10.5px">Comment SUN GLOW</div>
    <p class="post__text w6" style="left:29px;top:180px;font-size:12px">to join us!</p>
    <p class="post__handle" style="top:197px">@Maya Rivers Online</p>
  </article>

  <article class="post" style="left:726px;top:38px">
    <div class="post__photo post__photo--warm" role="img" aria-label="Smiling woman in olive swimsuit by an infinity pool"></div>
    <div class="post__frame post__frame--top"></div><div class="post__frame post__frame--bottom"></div>
    <div class="post__card"></div>
    <h2 class="post__text w7" style="top:72px;font-size:17px;line-height:16px">Need a<br>Jumpstart?</h2>
    <p class="post__text w6" style="left:27px;top:109px;font-size:9px;line-height:11px">We're Detoxing,<br>Burning Fat, and<br>getting snatched.</p>
    <div class="post__band" style="top:145px;height:14px;line-height:14px;font-size:10.5px">Comment SUN GLOW</div>
    <p class="post__text w6" style="left:29px;top:163px;font-size:11px;line-height:12px">to join us<br>On July 7th</p>
    <p class="post__handle" style="top:196px">@Maya Rivers Online</p>
  </article>

  <article class="post" style="left:957px;top:38px">
    <div class="post__photo post__photo--garden" role="img" aria-label="Woman in brown crochet swimsuit outdoors"></div>
    <div class="post__frame post__frame--top"></div><div class="post__frame post__frame--bottom"></div>
    <div class="post__card"></div>
    <h2 class="post__text w7" style="top:76px;font-size:15.5px;line-height:15.5px">Cravings,<br>Belly Fat, and<br>Water Weight?</h2>
    <div class="post__band" style="top:132px;height:13px;font-size:10px">Comment SUMMER</div>
    <p class="post__text w6" style="left:26px;top:151px;font-size:8px;line-height:9px">to join</p>
    <p class="post__text w6" style="left:26px;top:161px;font-size:11px;line-height:11.5px">The Sun Glow<br>Summer Reset</p>
    <p class="post__handle" style="top:194px">@Maya Rivers Online</p>
  </article>

  <!-- Row 2 -->
  <article class="post" style="left:31px;top:321px">
    <div class="post__photo post__photo--garden" role="img" aria-label="Woman in brown crochet dress on a lawn"></div>
    <div class="post__frame post__frame--top"></div><div class="post__frame post__frame--bottom"></div>
    <div class="post__card"></div>
    <h2 class="post__text w6" style="top:62px;font-size:13px;line-height:15.5px">If you feel like<br>you've let yourself<br>go lately,this is<br>your Jumpstart.</h2>
    <div class="post__band" style="top:131px;height:14px;line-height:14px;font-size:10.5px">Comment SUMMER</div>
    <p class="post__text w5" style="left:26px;top:148px;font-size:8px;line-height:9px">to join</p>
    <p class="post__text w6" style="left:26px;top:158px;font-size:10.5px;line-height:11.5px">The Sun Glow<br>Summer Reset</p>
    <p class="post__handle" style="top:190px">@Maya Rivers Online</p>
  </article>

  <article class="post" style="left:266px;top:321px">
    <div class="post__photo" role="img" aria-label="Woman in black bikini and sunglasses in a pool"></div>
    <div class="post__frame post__frame--top"></div><div class="post__frame post__frame--bottom"></div>
    <div class="post__card"></div>
    <h2 class="post__text w7" style="top:64px;font-size:17px;line-height:17px">Summer's Here</h2>
    <p class="post__text w5" style="top:83px;font-size:7.5px;line-height:8.5px">but your body doesn't<br>feel ready?</p>
    <p class="post__text w6" style="left:27px;top:101px;font-size:13px;line-height:12.5px">You're not<br>too Late.</p>
    <div class="post__band" style="top:131px;height:14px;line-height:14px;font-size:10.5px">Comment SUMMER</div>
    <p class="post__text w5" style="left:29px;top:148px;font-size:8px;line-height:9px">to join</p>
    <p class="post__text w6" style="left:29px;top:158px;font-size:10.5px;line-height:11.5px">The Sun Glow<br>Summer Reset</p>
    <p class="post__handle" style="top:190px">@Maya Rivers Online</p>
  </article>

  <article class="post" style="left:498px;top:321px">
    <div class="post__photo post__photo--warm" role="img" aria-label="Smiling woman in olive swimsuit and long mesh cover-up"></div>
    <div class="post__frame post__frame--top"></div><div class="post__frame post__frame--bottom"></div>
    <div class="post__card"></div>
    <h2 class="post__text" style="left:29px;top:66px;letter-spacing:0">
      <span class="w5" style="display:block;font-size:12px;line-height:14px">This SUN GLOW</span>
      <span class="wide" style="display:block;font-size:14.5px;line-height:14px">SUMMER</span>
      <span class="wide" style="display:block;font-size:14.5px;line-height:14px">RESET</span>
      <span class="wide" style="display:block;font-size:18px;line-height:17px">PLAN</span>
    </h2>
    <p class="post__text w5" style="left:29px;top:127px;font-size:6.5px;line-height:8.5px">is helping women drop pounds<br>and feel sexy again.</p>
    <div class="post__band" style="top:149px;height:14px;line-height:14px;font-size:10.5px;padding-left:30px">Comment SUMMER</div>
    <p class="post__text w6" style="left:34px;top:166px;font-size:11.5px">to Join Us</p>
    <p class="post__handle" style="top:189px">@Maya Rivers Online</p>
  </article>

  <article class="post" style="left:726px;top:321px">
    <div class="post__photo" role="img" aria-label="Woman in black bikini leaning on a pool edge"></div>
    <div class="post__frame post__frame--top"></div><div class="post__frame post__frame--bottom"></div>
    <div class="post__card"></div>
    <h2 class="post__text w6" style="top:63px;font-size:12.5px;line-height:13.8px">We're getting a<br>Tiny Waist,<br>Dropping<br>Pounds together.</h2>
    <p class="post__text w6" style="top:121px;font-size:12px">Don't miss this.</p>
    <div class="post__band" style="top:143px;height:14px;line-height:14px;font-size:10.5px;padding-left:22px">Comment SUN GLOW</div>
    <p class="post__text w6" style="left:27px;top:162px;font-size:12.5px">to Join Us</p>
    <p class="post__handle" style="top:190px">@Maya Rivers Online</p>
  </article>

  <article class="post" style="left:957px;top:321px">
    <div class="post__photo" role="img" aria-label="Smiling woman in leopard bikini at poolside"></div>
    <div class="post__frame post__frame--top"></div><div class="post__frame post__frame--bottom"></div>
    <div class="post__card"></div>
    <h2 class="post__text w6" style="top:66px;font-size:14px;line-height:15px">You don't need</h2>
    <p class="post__text w7" style="top:80px;font-size:20px;line-height:21px;color:#2a2a2a">Motivation.</p>
    <p class="post__text w5" style="top:104px;font-size:8px;line-height:9.5px">You need a Proven Plan<br>and some Accountability.</p>
    <div class="post__band" style="top:131px;height:14px;line-height:14px;font-size:10.5px;padding-left:20px">Comment SUN GLOW</div>
    <p class="post__text w6" style="left:26px;top:151px;font-size:11.5px;line-height:12.5px">to Join Us<br>On July 7th</p>
    <p class="post__handle" style="top:190px">@Maya Rivers Online</p>
  </article>

</main>
</body>
</html>
```